Hunting Ethics Organization Needs a Web Design with Logo Refresh

This project involves the creation of a website design including the homepage design, inside page design, and logo refinements. Our organization is Talvera, and we are a not-for-profit hunting ethics organization.
The focus of the new website design is to bring attention the mission of our organization, provide an overview of the areas where our organization deploys its resources to support the modern hunter, and to encourage visitors to support our organization by donating in support of the organization’s mission.
The winning design will be implemented in Wordpress by our in-house team. If you have questions about how any particular design element may translate to Wordpress, please feel free to post questions in response to this brief. In general, however, we’re more focused on the evolution and delivery of a strong overall design aesthetic – we’ll shoulder the responsibility of how we translate that design into Wordpress.
See attached design brief for full details.

```html
<!DOCTYPE html>
<html lang="en">
<head>
<meta charset="utf-8">
<title>Talvera – The Hunter's Institute</title>
<link rel="stylesheet" href="https://fonts.googleapis.com/css2?family=Ubuntu:wght@400;500&family=Open+Sans:ital,wght@0,400;1,400&display=swap">
<style>
:root{
  --olive:#a8a46a;
  --olive-dark:#9c9a62;
  --olive-band:#a29f64;
  --navy:#1e3a8f;
  --navy-label:rgba(32,40,110,.85);
  --ink:#2b2a14;
  --text:#555;
  --paper:#fafaf7;
  --white:#fff;
}
*{box-sizing:border-box;margin:0;padding:0}
html,body{width:800px;height:1200px;overflow:hidden}
body{position:relative;background:var(--paper);font-family:"Open Sans",sans-serif;color:var(--text)}
.abs{position:absolute}
.topbar{left:0;top:0;width:800px;height:27px;background:var(--olive)}
.social-dot{width:13px;height:13px;border-radius:50%;background:var(--white);top:7px}
.search{left:597px;top:5px;width:157px;height:16px;background:#8d8a55;border-radius:2px;color:#eee;font-size:8px;padding:3px 7px;font-family:"Ubuntu",sans-serif}
.header{left:0;top:27px;width:800px;height:67px;background:var(--white)}
.brand{left:47px;top:40px;display:flex;align-items:center;gap:8px}
.brand-mark{width:18px;height:18px;border-radius:50%;background:var(--olive)}
.brand-name{font-family:"Ubuntu",sans-serif;font-size:32px;color:var(--navy);letter-spacing:1px;line-height:1}
.brand-sub{left:77px;top:72px;font-family:"Ubuntu",sans-serif;font-size:9px;color:var(--navy);letter-spacing:.5px}
.nav{top:56px;font-family:"Ubuntu",sans-serif;font-size:10px;color:#555}
.donate{left:690px;top:51px;width:64px;height:23px;background:var(--navy);color:var(--white);font-family:"Ubuntu",sans-serif;font-size:10.5px;display:flex;align-items:center;justify-content:center;border-radius:2px}
.hero{left:0;top:94px;width:800px;height:408px;background:linear-gradient(100deg,#c9a874 0%,#b58f5c 40%,#6f6440 75%,#4a4a30 100%)}
.hero-caption{left:0;top:372px;width:358px;height:92px;background:rgba(168,164,106,.75);padding:6px 0 0 46px;font-family:"Ubuntu",sans-serif}
.hero-caption .l1{font-size:30px;color:var(--white);line-height:1.15}
.hero-caption .l2{font-size:38px;color:var(--ink);font-weight:500;line-height:1.1}
.mission{left:0;top:502px;width:800px;height:72px;background:var(--olive-band);display:flex;align-items:center;justify-content:center;text-align:center;font-family:"Ubuntu",sans-serif;font-size:19px;color:var(--ink);line-height:1.15;padding:0 90px}
.card{top:610px;width:226px;height:210px}
.card-label{left:0;bottom:9px;width:100%;height:36px;background:var(--navy-label);color:var(--white);font-family:"Ubuntu",sans-serif;font-size:14px;display:flex;align-items:center;justify-content:center}
h2{font-family:"Ubuntu",sans-serif;font-weight:400;font-size:18px;color:var(--navy)}
.welcome{left:47px;top:852px;width:480px}
.welcome p{font-size:9px;line-height:15.6px;margin-top:8px}
.welcome p+p{margin-top:16px}
.welcome a{color:var(--navy);font-style:italic;text-decoration:none}
.newsletter{left:548px;top:852px;width:206px}
.news-box{margin-top:8px;height:117px;background:#f0f0ec;border:1px solid #e2e2dc;padding:12px 14px}
.news-box p{font-size:9px;line-height:15.6px;color:#444}
.news-input{margin-top:8px;height:20px;background:var(--white);border:1px solid #d6d6d0;margin-left:-5px}
.subscribe{margin:11px 0 0 auto;width:68px;height:21px;background:var(--navy);color:var(--white);font-family:"Ubuntu",sans-serif;font-size:9.5px;display:flex;align-items:center;justify-content:center;border-radius:2px}
.wildlife{left:0;top:1035px;width:800px;height:78px;background:linear-gradient(180deg,rgba(156,154,98,0) 0%,rgba(156,154,98,.35) 45%,rgba(156,154,98,.8) 80%,var(--olive-dark) 100%)}
.footer{left:0;top:1112px;width:800px;height:88px;background:var(--olive-dark)}
.foot-link{top:1136px;font-family:"Ubuntu",sans-serif;font-size:9.5px;color:#222}
.copyright{left:49px;top:1162px;font-size:9px;color:#222}
.follow{left:645px;top:1136px;font-family:"Ubuntu",sans-serif;font-size:10px;color:#222}
.foot-dot{top:1152px;width:25px;height:25px;border-radius:50%;background:var(--white)}
</style>
</head>
<body>
<div class="abs topbar"></div>
<span class="abs social-dot" style="left:518px"></span>
<span class="abs social-dot" style="left:543px"></span>
<span class="abs social-dot" style="left:569px"></span>
<div class="abs search">Search</div>

<header class="abs header"></header>
<div class="abs brand"><span class="brand-mark"></span><span class="brand-name">TALVERA</span></div>
<div class="abs brand-sub">THE HUNTER'S INSTITUTE</div>
<nav>
<span class="abs nav" style="left:299px">About Us</span>
<span class="abs nav" style="left:367px">Hunting Ethics</span>
<span class="abs nav" style="left:458px">Conservation</span>
<span class="abs nav" style="left:544px">Get Involved</span>
<span class="abs nav" style="left:626px">Contact Us</span>
</nav>
<div class="abs donate">Donate</div>

<div class="abs hero" role="img" aria-label="Hunter in camouflage aiming a scoped rifle among tall golden reeds"></div>
<div class="abs hero-caption"><div class="l1">Protecting the future</div><div class="l2">of hunting</div></div>

<div class="abs mission">Protecting the future of hunting as leaders insetting the example for the modern hunter</div>

<div class="abs card" style="left:47px;background:linear-gradient(180deg,#7d7458 0%,#9aa36a 55%,#8f9a5a 100%)" role="img" aria-label="No hunting sign on a post in a grassy valley">
  <div class="abs card-label">Hunting Ethics</div></div>
<div class="abs card" style="left:288px;background:linear-gradient(180deg,#8e9a5c 0%,#b49a63 60%,#a38555 100%)" role="img" aria-label="Gazelle and cheetah in tall grass">
  <div class="abs card-label">Conservation</div></div>
<div class="abs card" style="left:528px;background:linear-gradient(180deg,#5f7a3e 0%,#7c7c55 55%,#6a6344 100%)" role="img" aria-label="Bowhunter in camouflage drawing a compound bow">
  <div class="abs card-label">Get Involved</div></div>

<section class="abs welcome">
  <h2>Welcome to Talvera</h2>
  <p>The Talvera Wildlife Federation is Talvera's oldest, largest and most effective conservation organization.&nbsp; Since 1948, we've led efforts to protect Talvera's abundant fish and wildlife, our natural lands and waters, and public access for hunting, fishing, and other outdoor recreation.</p>
  <p>Over the years, TWF has secured some of the Ridgeline State's most important conservation victories, including the strongest river access law in the region, a ban on confined wildlife farms, and protection of some of Talvera's most important wild lands. <a href="#">Read More</a></p>
</section>

<section class="abs newsletter">
  <h2>Newsletter</h2>
  <div class="news-box">
    <p>Below enter your email address and Subscribe our Newsletter</p>
    <div class="news-input"></div>
    <div class="subscribe">Subscribe</div>
  </div>
</section>

<div class="abs wildlife" role="img" aria-label="Row of wildlife silhouettes: birds, moose, deer, rhino, giraffe, elephant"></div>

<footer class="abs footer"></footer>
<span class="abs foot-link" style="left:49px">Home</span>
<span class="abs foot-link" style="left:96px">About Us</span>
<span class="abs foot-link" style="left:157px">Hunting Ethics</span>
<span class="abs foot-link" style="left:242px">Conservation</span>
<span class="abs foot-link" style="left:320px">Get Involved</span>
<span class="abs foot-link" style="left:396px">Contact Us</span>
<span class="abs foot-link" style="left:465px">Donate</span>
<div class="abs copyright">© copyright 2015 by talvera. All rights reserved.</div>
<div class="abs follow">Follow us</div>
<span class="abs foot-dot" style="left:645px"></span>
<span class="abs foot-dot" style="left:687px"></span>
<span class="abs foot-dot" style="left:728px"></span>
</body>
</html>
```